Finch Haulage Ltd

We need an A5 size (UK size) flyer to advertise our new business which is called Finch Haulage.
Domestic and Commercial Waste Clearance Services.
Please have the question in bold "Do you have a pile of junk you need to dispose of?"
We collect all kinds of junk or rubbish from homes and businesses across Kent, Sussex and South London.
No fuss, no mess!
A low cost, hassle free alternative to skip hire.
Licensed by the Landcare Board and fully insured (this can be in small print at the bottom).
Please put the Recycle symbol somewhere.
Our tagline on our vehicle is "We Clear More, For Less!"
We'd like the flyer to be bold and eye-catching (to catch the eye of the homeowner or business owner while it's sitting on their doormat).
We need our telephone, website and email to be prominent. Maybe saying "Call today for a free quote"
Tel. 01734 586019
Email: info@finchhaulage.example.co.uk
www.finchhaulage.example.co.uk
Target Market(s)
Our market will be homes and small businesses around Kent, Sussex and South London.

```html
<!DOCTYPE html>
<html lang="en">
<head>
<meta charset="utf-8">
<title>Finch Haulage – Waste Clearance Flyer</title>
<link href="https://fonts.googleapis.com/css2?family=Anton&family=Arimo:wght@400;700&display=swap" rel="stylesheet">
<style>
  :root {
    --page-bg: #e6e6e6;
    --paper: #ffffff;
    --brand-green: #1fad4f;
    --ink-grey: #555659;
    --band-slate: #5b6785;
    --water-teal: #2a9c86;
    --water-deep: #1f8a76;
    --on-dark: #ffffff;
  }
  * { box-sizing: border-box; margin: 0; padding: 0; }
  html, body {
    width: 1200px; height: 960px; overflow: hidden;
    background: var(--page-bg);
    font-family: "Arimo", Arial, sans-serif;
  }
  .flyer {
    position: absolute; left: 110px; top: 10px;
    width: 980px; height: 940px;
    background: var(--paper);
    display: flex; flex-direction: column; align-items: center;
    overflow: hidden;
    box-shadow: 0 2px 10px rgba(0,0,0,.15);
  }
  .brand {
    margin-top: 36px;
    display: flex; align-items: center; gap: 18px;
  }
  .brand-dot {
    width: 32px; height: 32px; border-radius: 50%;
    background: var(--brand-green);
  }
  .brand-name {
    font-weight: 700; font-size: 60px; letter-spacing: 2px;
    color: var(--ink-grey); line-height: 1;
  }
  .tagline {
    margin-top: 10px; font-size: 24px; color: var(--ink-grey);
  }
  .headline {
    margin-top: 20px;
    font-family: "Anton", "Arial Narrow", sans-serif;
    font-size: 56px; line-height: 1.05; text-transform: uppercase;
    color: var(--brand-green); text-align: center;
  }
  .call-us {
    margin-top: 14px; font-size: 32px; color: var(--ink-grey); line-height: 1.1;
  }
  .call-us strong, .accent { color: var(--brand-green); font-weight: 700; }
  .call-us strong { font-size: 42px; }
  .intro {
    margin-top: 2px; width: 900px;
    font-size: 28px; line-height: 1.2; color: var(--ink-grey); text-align: center;
  }
  .intro .accent { font-weight: 400; font-size: 38px; }
  .no-fuss {
    margin-top: 14px; font-size: 36px; color: var(--ink-grey); line-height: 1.1;
  }
  .no-fuss .accent { font-size: 48px; }
  .prices {
    font-size: 34px; color: var(--ink-grey); text-transform: uppercase; line-height: 1.15;
  }
  .skip-alt {
    margin-top: 4px; font-size: 24px; color: var(--brand-green); font-weight: 700;
  }
  .waterline {
    position: absolute; left: 0; right: 0; top: 660px; height: 40px;
    background: linear-gradient(to bottom, rgba(31,173,79,0) 0%, rgba(31,173,79,.55) 100%);
  }
  .contact-area {
    position: absolute; left: 0; right: 0; top: 700px; bottom: 0;
    background: linear-gradient(to bottom, var(--water-teal), var(--water-deep));
    color: var(--on-dark); text-align: center;
  }
  .quote-band {
    height: 56px; background: var(--band-slate);
    display: flex; align-items: center; justify-content: center;
    font-size: 26px; text-transform: uppercase; letter-spacing: .5px;
  }
  .contact-list {
    list-style: none; margin-top: 14px;
    font-weight: 700; font-size: 27px; line-height: 1.4;
  }
  .licence {
    margin-top: 10px; font-size: 18px;
    display: flex; align-items: center; justify-content: center; gap: 10px;
  }
  .recycle-icon { width: 28px; height: 28px; flex: none; }
</style>
</head>
<body>
  <main class="flyer">
    <header class="brand">
      <span class="brand-dot"></span>
      <span class="brand-name">Finch Haulage</span>
    </header>
    <p class="tagline">We Clear More, For Less!</p>

    <h1 class="headline">Do you have a pile of junk you<br>need to dispose of?</h1>

    <p class="call-us">Call <strong>US!</strong></p>
    <p class="intro">We collect <span class="accent">ALL</span> kinds of junk or rubbish, from homes and businesses across Kent, Sussex and South London, sweep the area clean and take the rubbish away.</p>

    <p class="no-fuss"><span class="accent">NO</span> fuss, <span class="accent">NO</span> mess.</p>
    <p class="prices">Very competitive prices</p>
    <p class="skip-alt">A low cost, hassle free alternative to skip hire.</p>

    <div class="waterline" role="img" aria-label="Green reptiles swimming at the water's surface"></div>

    <section class="contact-area" role="img" aria-label="Rippling teal water surface">
      <div class="quote-band">Call today for a free, no obligation quote</div>
      <ul class="contact-list">
        <li>Telephone: 01734 586019</li>
        <li>Email: info@finchhaulage.example.co.uk</li>
        <li>www.finchhaulage.example.co.uk</li>
      </ul>
      <p class="licence">
        <svg class="recycle-icon" viewBox="0 0 32 32" aria-hidden="true">
          <g fill="none" stroke="#ffffff" stroke-width="3" stroke-linecap="round" stroke-linejoin="round">
            <path d="M9 12 L13 5 Q16 1 19 5 L22 10"/>
            <path d="M19 10 L23 11 L24 7"/>
            <path d="M25 16 L28 23 Q29 27 24 27 L17 27"/>
            <path d="M20 24 L17 27 L20 30"/>
            <path d="M11 27 L6 27 Q2 27 4 22 L7 17"/>
            <path d="M4 18 L7 16 L10 19"/>
          </g>
        </svg>
        <span>Licensed by the Landcare Board and fully insured. We Also Recycle.</span>
      </p>
    </section>
  </main>
</body>
</html>
```